I need to rebrand my public user portal for a new/modern look and feel

I want to take my current user web portal and redesign the look of it. I have included 2 samples of my current user portal and would like options to create a new functional look. This main page below will modify based on the tabs on the top left. Any questions please ask.

```html
<!DOCTYPE html>
<html lang="en">
<head>
<meta charset="utf-8">
<title>Student Portal Dashboard</title>
<link href="https://fonts.googleapis.com/css2?family=Poppins:wght@400;500;600&display=swap" rel="stylesheet">
<style>
:root{
  --page:#7590b0;
  --crimson:#861618;
  --crimson-dark:#6c1219;
  --olive:#7d6a2f;
  --olive-dark:#5e4f20;
  --surface:#ffffff;
  --canvas:#f3f4f8;
  --notice:#fdf8dc;
  --row-tint:#fff2f2;
  --ink:#1f1f2b;
  --muted:#6b6b78;
  --line:#e2e2e8;
}
*{box-sizing:border-box;margin:0;padding:0}
html,body{width:1200px;height:875px;overflow:hidden}
body{background:var(--page);font-family:"Poppins",sans-serif;color:var(--ink);position:relative}
.app{position:absolute;left:27px;top:27px;width:1146px;height:784px;border-radius:25px;overflow:hidden;background:var(--canvas);display:flex}
.sidebar{width:216px;background:var(--crimson);position:relative;flex:none}
.brand{position:absolute;left:23px;top:40px;display:flex;align-items:center;gap:8px;color:#fff;font-weight:600;font-size:15px;letter-spacing:.3px}
.brand-dot{width:14px;height:14px;border-radius:50%;background:#fff}
.nav{position:absolute;top:94px;left:12px;right:0;list-style:none}
.nav li{height:42px;margin-bottom:3px;display:flex;align-items:center;gap:13px;padding-left:12px;color:#fff;font-size:12px;border-radius:10px 0 0 10px}
.nav li.active{background:var(--olive)}
.nav svg{width:18px;height:18px;stroke:#fff;fill:none;stroke-width:1.5}
.settings{position:absolute;left:23px;top:715px;width:122px;height:47px;background:var(--olive);border-radius:6px;display:flex;align-items:center;justify-content:center;gap:9px;color:#fff;font-weight:600;font-size:12px;box-shadow:0 3px 0 rgba(0,0,0,.15)}
.settings svg{width:18px;height:18px;stroke:#fff;fill:none;stroke-width:1.5}
.main{flex:1;position:relative}
.topbar{height:72px;background:var(--surface);position:relative}
.search{position:absolute;left:47px;top:15px;width:349px;height:36px;background:#f3f3f5;border-radius:5px;display:flex;align-items:center;gap:12px;padding-left:14px;color:var(--muted);font-size:12px}
.search svg{width:18px;height:18px;stroke:#555;fill:none;stroke-width:1.5}
.user{position:absolute;right:30px;top:17px;display:flex;align-items:center;gap:14px;font-size:12px}
.bell{position:relative;width:22px;height:26px;margin-right:2px}
.bell svg{width:22px;height:26px;stroke:#444;fill:none;stroke-width:1.4}
.bell i{position:absolute;right:1px;top:1px;width:6px;height:6px;border-radius:50%;background:#e0474c}
.avatar{width:36px;height:36px;border-radius:50%;background:radial-gradient(circle at 50% 40%,#c89a86,#4b2a24)}
.chev{width:14px;height:14px;stroke:#333;fill:none;stroke-width:1.5}
.card{position:absolute;left:47px;width:848px;background:var(--surface);border-radius:10px;overflow:hidden;box-shadow:0 2px 6px rgba(0,0,0,.08)}
.card-head{height:54px;background:var(--crimson);position:relative;color:#fff;font-weight:600;font-size:11.5px}
.card-title{position:absolute;left:26px;top:50%;transform:translateY(-50%)}
.card-label{position:absolute;left:0;right:0;text-align:center;top:50%;transform:translateY(-50%)}
.add-btn{position:absolute;right:9px;top:10px;width:145px;height:36px;background:var(--crimson-dark);border-radius:5px;display:flex;align-items:center;justify-content:center;gap:12px;font-size:12px;font-weight:600}
.add-btn svg{width:13px;height:13px;stroke:#fff;fill:none;stroke-width:1.6}
.empty{height:82px;display:flex;align-items:center;justify-content:center}
.notice{width:185px;height:40px;background:var(--notice);border-radius:5px;display:flex;align-items:center;justify-content:center;font-size:10.5px}
.badge{position:absolute;left:409px;top:225px;width:40px;height:40px;border-radius:50%;background:#fff;border:2px solid #2b4e9a}
table{width:100%;border-collapse:collapse;font-size:10.5px;text-align:center}
th{background:var(--olive);color:#fff;font-weight:500;height:46px;border-right:1px solid #ffffff55}
th:last-child,td:last-child{border-right:none}
td{border-right:1px solid var(--line)}
tr.tint td{background:var(--row-tint)}
.action{display:inline-flex;align-items:center;justify-content:center;gap:18px;width:127px;height:41px;border-radius:20px;background:var(--olive);color:#fff;font-size:10.5px;box-shadow:0 3px 0 var(--olive-dark)}
.action b{width:0;height:0;border-left:3.5px solid transparent;border-right:3.5px solid transparent;border-top:4px solid #fff}
</style>
</head>
<body>
<div class="app">
  <aside class="sidebar">
    <div class="brand"><span class="brand-dot"></span>Meridian Works</div>
    <ul class="nav">
      <li class="active"><svg viewBox="0 0 24 24"><path d="M3 18a9 9 0 0 1 18 0z"/><path d="M12 18l5-6"/></svg>Dashboard</li>
      <li><svg viewBox="0 0 24 24"><rect x="5" y="4" width="14" height="17" rx="2"/><path d="M9 4h6v3H9zM8 12h8M8 16h6"/></svg>Application</li>
      <li><svg viewBox="0 0 24 24"><rect x="3" y="5" width="15" height="12" rx="1"/><path d="M6 9h6M6 13h4"/><circle cx="17" cy="15" r="3"/></svg>Transcript Request</li>
      <li><svg viewBox="0 0 24 24"><circle cx="10" cy="8" r="4"/><path d="M3 20a7 7 0 0 1 12-4M16 17l2 2 4-4"/></svg>New Hire packet</li>
    </ul>
    <div class="settings"><svg viewBox="0 0 24 24"><circle cx="12" cy="12" r="3"/><path d="M12 3l2 2h3v3l2 2-2 2v3h-3l-2 2-2-2H7v-3l-2-2 2-2V5h3z"/></svg>Settings</div>
  </aside>
  <main class="main">
    <header class="topbar">
      <div class="search"><svg viewBox="0 0 24 24"><circle cx="11" cy="11" r="7"/><path d="M16 16l4 4"/></svg>Search for anything...</div>
      <div class="user">
        <div class="bell"><svg viewBox="0 0 24 28"><path d="M5 20V12a7 7 0 0 1 14 0v8l2 2H3zM10 24a2 2 0 0 0 4 0"/></svg><i></i></div>
        <span>Nora Whitfield</span>
        <div class="avatar" role="img" aria-label="User profile photo"></div>
        <svg class="chev" viewBox="0 0 14 14"><path d="M2 5l5 5 5-5"/></svg>
      </div>
    </header>

    <section class="card" style="top:109px">
      <div class="card-head"><span class="card-title">SCSSDEMO19</span><span class="card-label">Students</span>
        <div class="add-btn">Add student via <svg viewBox="0 0 14 14"><path d="M2 5l5 5 5-5"/></svg></div></div>
      <div class="empty"><div class="notice">No record found</div></div>
    </section>

    <div class="badge" style="left:669px;top:271px"></div>

    <section class="card" style="top:328px">
      <div class="card-head"><span class="card-title">RCVTS</span><span class="card-label">Students</span>
        <div class="add-btn">Add student via <svg viewBox="0 0 14 14"><path d="M2 5l5 5 5-5"/></svg></div></div>
      <div class="empty"><div class="notice">No record found</div></div>
    </section>

    <section class="card" style="top:490px">
      <div class="card-head"><span class="card-title">GRADELINE DEMO TEST</span><span class="card-label">Students</span>
        <div class="add-btn">Add student via <svg viewBox="0 0 14 14"><path d="M2 5l5 5 5-5"/></svg></div></div>
      <table>
        <colgroup><col style="width:224px"><col style="width:131px"><col style="width:106px"><col style="width:213px"><col></colgroup>
        <tr><th>Name</th><th>Grade</th><th>Year</th><th>School</th><th>Action</th></tr>
        <tr style="height:57px"><td>SCVIEW8108 Testing</td><td>KG</td><td>2024</td><td>Testing</td><td><span class="action">Create / Edit <b></b></span></td></tr>
        <tr class="tint" style="height:47px"><td>Marta Ellison</td><td>11</td><td>2024</td><td>Tesdt</td><td><span class="action">Create / Edit <b></b></span></td></tr>
        <tr style="height:66px"><td>Regression Test</td><td>09</td><td>2024</td><td>Northgate High School</td><td><span class="action">Create / Edit <b></b></span></td></tr>
      </table>
    </section>
  </main>
</div>
</body>
</html>
```